Веб-сайт для застройщика под греческую золотую визу Veltaroon.gr
застройщик под греческую золотую визу Veltaroon.gr
Veltaroon.gr
https://morvilo-estates.com/
https://tpk.example/
Veltaroon Development IKE — Website Design Brief
Домен: veltaroon.gr
Название Veltaroon является авторским сочетанием слов:
Hellenic
Premium
Название должно ассоциироваться с:
premium Mediterranean lifestyle
boutique investment real estate
комфортом и эстетикой
Это можно опционально и ненавязчиво обыгрывать в дизайне:
через typography
через premium визуальные акценты
через Mediterranean aesthetic
через сочетание natural + premium visual language
Важно:
Бренд не должен выглядеть overly luxury или “gold-plated wealth style”.
Основной акцент:
tasteful premium
calm confidence
boutique sophistication
1. О компании
Veltaroon Development IKE — девелоперская компания в Греции, которая занимается:
покупкой и реновацией зданий
созданием boutique apartments
продажей недвижимости под Greek Golden Visa
дальнейшим управлением арендой для инвесторов
2. Основная идея сайта
Главный акцент:
Greek Golden Visa
инвестиции в недвижимость в Греции
получение ВНЖ в Европе
комфортный Mediterranean lifestyle
Важно показать, что компания делает проекты «с душой»:
натуральные материалы
светлое дерево
мягкий olive green
уютные современные интерьеры
boutique Mediterranean aesthetics
3. Сайт должен выглядеть
premium
trustworthy
modern
investment-oriented
4. Сайт НЕ должен выглядеть
как агентство недвижимости
как дешёвый Golden Visa landing page
как обычная строительная компания
5. Целевая аудитория
Средний возраст клиентов: 45+ лет, семейные инвесторы, часто ищущие решение для всей семьи.
Инвесторы и семьи из:
Китай
Турция
СНГ
Middle East
Основная цель клиентов:
получение ВНЖ в Европе через Greek Golden Visa
покупка доходной недвижимости
инвестиции в недвижимость в ЕС
6. Основное меню
Greek Golden Visa или просто Golden Visa
Projects
Investors
Partners
Contact (внутри Contact раздела будет вставка About Us либо же вставка будет сразу на главной странице - на ваше усмотрение)
Дополнительно:
Client Login (отдельный кабинет для покупателей квартир / инвесторов)
7. Языки сайта
EN (по умолчанию)
GR
RU
中文
TR
8. Визуальная стилистика
Эстетика
Mediterranean vibe
boutique living vibe
premium natural materials
Цвета:
olive green
warm white
beige
soft stone grey
(Цвета даны справочно и могут адаптироваться дизайнером)
UI стиль:
clean
calm
ВАЖНО:
Полное техническое задание не влезло в описание и размещено в открытом виде на внешнем файлообменнике в текстовом файле:
https://filebarrow.example/k4Rq8
или
https://sklad-faylov.example/7pLmz

```html
<!DOCTYPE html>
<html lang="en">
<head>
<meta charset="utf-8">
<title>Veltaroon Development — Golden Visa Investments</title>
<link rel="stylesheet" href="https://fonts.googleapis.com/css2?family=EB+Garamond:wght@400;500;600&family=Manrope:wght@400;500;600&display=swap">
<style>
:root{
  --olive:#4a4a08;
  --olive-deep:#3f3f05;
  --bg:#eeedea;
  --warm-white:#f3f1ee;
  --sand:#9c8462;
  --label:#8a7250;
  --ink:#3e3c1c;
  --cream:#f1ecd8;
}
*{box-sizing:border-box;margin:0;padding:0}
html,body{width:1200px;height:3460px;overflow:hidden;background:var(--bg)}
body{font-family:"Manrope",sans-serif;color:var(--ink)}
.canvas{position:relative;width:1200px;height:3460px;overflow:hidden;background:var(--bg)}
.abs{position:absolute}
.serif{font-family:"EB Garamond",serif;color:var(--olive);font-weight:500}
.label{font-family:"Manrope",sans-serif;font-size:17px;color:var(--label);letter-spacing:.2px;text-transform:uppercase;font-weight:500}
.learn{font-size:11px;color:var(--label);display:flex;align-items:center;gap:8px}
.learn svg{display:block}
.photo{position:absolute}

/* header */
.hero{position:absolute;left:0;top:0;width:1200px;height:673px;background:var(--warm-white);overflow:hidden}
.hero-photo{position:absolute;left:420px;top:0;width:780px;height:673px;
  background:
   linear-gradient(to right,var(--warm-white) 0%,rgba(243,241,238,.7) 14%,rgba(243,241,238,0) 36%),
   linear-gradient(to bottom,#efe2d6 0%,#e6c9ad 30%,#b8957a 48%,#8c8a72 60%,#c9b49d 70%,#5e8fa4 86%,#3f6e82 100%)}
.logo{display:flex;align-items:center;gap:8px;font-family:"EB Garamond",serif;font-weight:600;letter-spacing:2.5px;font-size:17px;color:var(--olive)}
.logo i{width:12px;height:12px;background:currentColor;display:block}
.nav{position:absolute;top:43px;font-size:11px;color:var(--olive);letter-spacing:.2px}
.btn{position:absolute;display:flex;align-items:center;justify-content:center;font-size:8px;color:var(--cream)}

/* band */
.band{position:absolute;left:0;top:673px;width:1200px;height:171px;background:var(--olive)}
.band-item{position:absolute;top:40px;width:200px;margin-left:-100px;text-align:center;color:#e6e1c9;font-size:16px;line-height:21px}
.band-item svg{display:block;margin:0 auto 10px}

.para{position:absolute;font-size:18px;line-height:24.8px;color:var(--ink)}
.stat-cap{position:absolute;top:2156px;font-size:16px;line-height:19px;color:var(--ink)}
.news-card{position:absolute;top:2815px;width:307px}
.news-card .img{height:170px}
.news-meta{display:flex;justify-content:space-between;margin-top:14px;font-size:13px;color:var(--label)}
.news-title{margin-top:18px;font-size:17px;line-height:21px;color:var(--olive);font-weight:500}
.news-card .learn{margin-top:10px}

.footer{position:absolute;left:0;top:3135px;width:1200px;height:325px;background:var(--olive);color:#e9e4cf}
.footer .logo{color:#efeadb}
.fcol{position:absolute;top:58px;font-size:11px;line-height:14px}
.fcol li{list-style:none;height:40px}
</style>
</head>
<body>
<div class="canvas">

<!-- HERO -->
<section class="hero">
  <div class="hero-photo" role="img" aria-label="Seaside villa terrace with infinity pool and lounge sofas at sunset over the Greek coast"></div>
  <div class="abs logo" style="left:110px;top:40px">VELTAROON<i></i></div>
  <span class="nav" style="left:317px">GOLDEN VISA</span>
  <span class="nav" style="left:433px">PROJECTS</span>
  <span class="nav" style="left:531px">INVESTORS</span>
  <span class="nav" style="left:634px">PARTNERS</span>
  <span class="nav" style="left:732px">CONTACT</span>
  <span class="nav" style="left:826px">ABOUT US</span>
  <svg class="abs" style="left:1029px;top:40px" width="17" height="19" viewBox="0 0 17 19" fill="none" stroke="#4a4a08" stroke-width="1.4"><circle cx="8.5" cy="6" r="4.5"/><path d="M1 18c0-4 3.4-6.5 7.5-6.5S16 14 16 18"/></svg>
  <span class="nav" style="left:1097px">EN ▲</span>

  <div class="abs serif" style="left:109px;top:193px;font-size:22px;color:var(--label);font-weight:400">Premium Greek Living</div>
  <h1 class="abs serif" style="left:107px;top:222px;font-size:84px;line-height:81px;font-weight:600">Golden Visa<br>Investments</h1>
  <p class="abs" style="left:109px;top:423px;font-size:19px;line-height:26px;color:var(--ink)">Boutique residences thought fully designed<br>for modern living and long-term investment</p>
  <div class="btn" style="left:109px;top:535px;width:176px;height:51px;background:var(--olive)">Explore Projects Greek</div>
  <div class="btn" style="left:359px;top:535px;width:176px;height:51px;background:var(--sand)">Golden Visa</div>
</section>

<!-- SERVICES BAND -->
<section class="band">
  <div class="band-item" style="left:222px">
    <svg width="26" height="28" viewBox="0 0 26 28" fill="none" stroke="#e6e1c9" stroke-width="1.2"><path d="M3 27V14M8 27V10M13 27V6c0-3 6-3 6 0v4M18 27V15"/></svg>
    Purchasing<br>and renovating<br>buildings</div>
  <div class="band-item" style="left:460px">
    <svg width="26" height="28" viewBox="0 0 26 28" fill="none" stroke="#e6e1c9" stroke-width="1.2"><path d="M3 27V12M8 27V12M13 27V12M18 27V12M23 27V12"/><circle cx="13" cy="4" r="1" fill="#e6e1c9"/></svg>
    Creating boutique<br>apartments</div>
  <div class="band-item" style="left:703px">
    <svg width="26" height="28" viewBox="0 0 26 28" fill="none" stroke="#e6e1c9" stroke-width="1.2"><path d="M4 3h18M4 7h18M7 9v16M11 9v16M15 9v16M19 9v16M4 27h18"/></svg>
    Selling property<br>under the Greek<br>Golden visa</div>
  <div class="band-item" style="left:943px">
    <svg width="30" height="28" viewBox="0 0 30 28" fill="none" stroke="#e6e1c9" stroke-width="1.2"><circle cx="15" cy="14" r="13"/><path d="M9 8v12M13 6v16M17 6v16M21 8v12"/></svg>
    Managing rentals<br>for investors</div>
</section>

<!-- PROJECTS -->
<div class="abs label" style="left:86px;top:869px">Projects</div>
<h2 class="abs serif" style="left:86px;top:888px;font-size:56px;line-height:62px">Athens Residence</h2>
<div class="abs" style="left:86px;top:957px;font-size:16px;color:var(--label);font-weight:500">12 Kalamidou Street, Athens</div>
<div class="abs" style="left:816px;top:968px;font-size:21px;color:var(--label)">Athens Hall</div>

<div class="photo" style="left:87px;top:1007px;width:687px;height:391px;background:linear-gradient(160deg,#cdbfa6 0%,#e4d6c1 30%,#9aa4a2 48%,#b49d82 70%,#6f5a43 100%)" role="img" aria-label="Bright living room with arched openings, plants and a wooden coffee table overlooking the sea"></div>
<div class="photo" style="left:805px;top:1007px;width:325px;height:211px;background:linear-gradient(170deg,#c9b39a 0%,#e0c9ae 35%,#8d9095 55%,#b8a48c 75%,#7e6b58 100%)" role="img" aria-label="Lounge with floor-to-ceiling windows and sea view at sunset"></div>
<div class="photo" style="left:805px;top:1246px;width:325px;height:153px;background:linear-gradient(175deg,#b9c6cf 0%,#cdd5d8 35%,#6f8fa3 55%,#c7b9a4 78%,#8b7a64 100%)" role="img" aria-label="Living area with panoramic glazing facing an island in the sea"></div>
<div class="abs learn" style="left:814px;top:1423px;font-size:10px">All projects
  <svg width="24" height="6" viewBox="0 0 24 6" fill="none" stroke="#8a7250"><path d="M0 3h23M20 0.5l3 2.5-3 2.5"/></svg></div>

<p class="para" style="left:86px;top:1423px">This elegant residence in Athens perfectly combines contemporary<br>architectural design with the timeless allure of the Mediterranean.</p>
<div class="abs learn" style="left:86px;top:1482px">Learn more
  <svg width="24" height="6" viewBox="0 0 24 6" fill="none" stroke="#8a7250"><path d="M0 3h23M20 0.5l3 2.5-3 2.5"/></svg></div>

<!-- GOLDEN VISA -->
<div class="abs label" style="left:86px;top:1523px">Golden Visa</div>
<h2 class="abs serif" style="left:86px;top:1548px;font-size:56px;line-height:62px">Your Gateway to Europe</h2>
<div class="photo" style="left:87px;top:1630px;width:499px;height:363px;background:linear-gradient(160deg,#d8c6ad 0%,#ece0cf 35%,#a8a598 50%,#c7b193 70%,#80684d 100%)" role="img" aria-label="Sunlit arched living room with cream sofas and sea view"></div>
<p class="para" style="left:630px;top:1630px;width:495px">The Greek Golden Visa is a residency-by-investment program offering a five-year, renewable residence permit to non-EU citizens who make a significant financial contribution to the Greek economy.<br>The program's main advantages include granting residency to the main investor as well as their immediate family (spouse, children, and parents), providing visa-free travel throughout the Schengen Area, and having no minimum stay requirement to maintain the residency status, making it one of Europe's most flexible and popular investment migration schemes.</p>
<div class="abs learn" style="left:629px;top:1933px">Learn more
  <svg width="24" height="6" viewBox="0 0 24 6" fill="none" stroke="#8a7250"><path d="M0 3h23M20 0.5l3 2.5-3 2.5"/></svg></div>

<!-- STATS -->
<div class="abs" style="left:87px;top:2028px;width:499px;height:111px;background:var(--olive)"></div>
<div class="abs serif" style="left:137px;top:2042px;font-size:42px;line-height:50px;color:#f1ecdc">€250K+</div>
<div class="abs serif" style="left:407px;top:2034px;font-size:40px;line-height:48px;color:#f1ecdc">yield</div>
<div class="abs serif" style="left:407px;top:2084px;font-size:40px;line-height:48px;color:#f1ecdc">10–15%</div>
<div class="abs serif" style="left:668px;top:2048px;font-size:66px;line-height:70px">5%</div>
<div class="abs serif" style="left:889px;top:2048px;font-size:62px;line-height:70px">3 years</div>
<div class="stat-cap" style="left:164px">investment<br>threshold</div>
<div class="stat-cap" style="left:388px">per annum (depending<br>on the market)</div>
<div class="stat-cap" style="left:642px">with a guaranteed<br>return per annum</div>
<div class="stat-cap" style="left:884px">for payments are made<br>by the company</div>

<!-- INVESTORS -->
<div class="abs label" style="left:86px;top:2257px">Investors</div>
<h2 class="abs serif" style="left:88px;top:2290px;font-size:56px;line-height:54px">A clear path<br>to your residency<br>and returns</h2>
<p class="abs" style="left:86px;top:2467px;font-size:14.5px;line-height:19.7px;color:var(--ink)">By choosing a government-approved program, investors<br>can secure a permanent home for their families while<br>simultaneously benefiting from robust capital growth<br>and rental returns.</p>
<div class="abs learn" style="left:86px;top:2555px">Learn more
  <svg width="24" height="6" viewBox="0 0 24 6" fill="none" stroke="#8a7250"><path d="M0 3h23M20 0.5l3 2.5-3 2.5"/></svg></div>
<div class="btn" style="left:87px;top:2604px;width:210px;height:45px;background:var(--olive);font-size:13px">Invest in Greece</div>
<div class="photo" style="left:562px;top:2276px;width:551px;height:345px;background:linear-gradient(165deg,#a9876a 0%,#e0bd8a 30%,#b88b5a 50%,#7a5738 72%,#c4a27a 100%)" role="img" aria-label="Golden-hour living room with glass wall opening onto a white villa terrace by the sea"></div>

<!-- NEWS -->
<div class="abs label" style="left:86px;top:2693px">Golden Visa News</div>
<h2 class="abs serif" style="left:86px;top:2722px;font-size:56px;line-height:62px">Stay informed. Stay Ahead</h2>

<article class="news-card" style="left:87px">
  <div class="img" style="background:linear-gradient(170deg,#8e8f86 0%,#b4ada0 35%,#3f8aa0 55%,#d8d3c8 80%,#a8a196 100%)" role="img" aria-label="Aerial view of a white island village above a turquoise bay"></div>
  <div class="news-meta"><span>REGISTRATION</span><span>May 15, 2026</span></div>
  <div class="news-title">Greece Extands Golden Visa Programm<br>Through 2025</div>
  <div class="learn">Learn more <svg width="24" height="6" viewBox="0 0 24 6" fill="none" stroke="#8a7250"><path d="M0 3h23M20 0.5l3 2.5-3 2.5"/></svg></div>
</article>
<article class="news-card" style="left:446px">
  <div class="img" style="background:linear-gradient(175deg,#7da0bd 0%,#a9bfcf 35%,#e2d8c8 55%,#a28568 78%,#5d7f8a 100%)" role="img" aria-label="Modern white residential building with balconies and pool"></div>
  <div class="news-meta"><span>MARKET INSIDE</span><span>May 2, 2026</span></div>
  <div class="news-title">Athens Real Estate Market Shows<br>Strong Grouwth in 2024</div>
  <div class="learn">Learn more <svg width="24" height="6" viewBox="0 0 24 6" fill="none" stroke="#8a7250"><path d="M0 3h23M20 0.5l3 2.5-3 2.5"/></svg></div>
</article>
<article class="news-card" style="left:806px">
  <div class="img" style="background:linear-gradient(140deg,#1f3550 0%,#2c4a6b 45%,#1a2d44 75%,#4b5a66 100%)" role="img" aria-label="Close-up of a dark blue passport cover"></div>
  <div class="news-meta"><span>GUIDE</span><span>Aprile 21, 2026</span></div>
  <div class="news-title">Step by step: How to Obtain Greece<br>Golden Visa</div>
  <div class="learn">Learn more <svg width="24" height="6" viewBox="0 0 24 6" fill="none" stroke="#8a7250"><path d="M0 3h23M20 0.5l3 2.5-3 2.5"/></svg></div>
</article>

<!-- FOOTER -->
<footer class="footer">
  <div class="abs logo" style="left:54px;top:55px">VELTAROON<i></i></div>
  <ul class="fcol" style="left:278px">
    <li>GOLDEN VISA</li><li>PROJECTS</li><li>INVESTORS</li><li>PARTNERS</li><li>CONTACT</li><li>ABOUT US</li>
  </ul>
  <div class="fcol" style="left:531px;line-height:17px">
    Lyrovou str. 18,<br>Athens 115 21, Greece
    <div style="margin-top:6px">Phone: +30 210 555 0142</div>
    <div style="margin-top:23px">E-male: hello@veltaroon.gr</div>
  </div>
  <ul class="fcol" style="left:779px">
    <li>PRIVACY POLICY</li><li>COOKIE POLICY</li><li>TERMS &amp; CONDITIONS</li><li>DISCLAIMER</li><li>GDPR COMPLIANCE</li>
  </ul>
  <svg class="abs" style="left:1025px;top:56px" width="15" height="17" viewBox="0 0 17 19" fill="none" stroke="#e9e4cf" stroke-width="1.4"><circle cx="8.5" cy="6" r="4.5"/><path d="M1 18c0-4 3.4-6.5 7.5-6.5S16 14 16 18"/></svg>
  <div class="abs" style="left:1090px;top:59px;font-size:11px">EN ▲</div>
</footer>

</div>
</body>
</html>
```